FR / EN Beekeeper research design packaging / label; Beekeeper looking for a design package

I need as a beekeeper to create a design to better showcase my honey. Indeed I work in a natural environment of high quality on a hill called "Waldhofen" (many flowers different fields, few pesticides, ...). I practice a beekeeping respectful of the bee and in a traditional way. I produce a high quality honey (luxury product) for a wealthy clientele looking for good health products, ... The main label should contain only the following text (accompanied by an image): The Waldhofen Honey A variant would also be useful for my production of mead (alcohol from the fermentation of honey): The Waldhofen mead In terms of form, given the target audience, I thought I was moving towards a modern label against a background black and with golden patterns. An example is the honey of the wonders attached, we find a honey assimilated as a real luxury product. Same in the Cuvée Lorenzo Pavetti attachment. I would like to move towards these tones of colors by adding a touch more "champêtre" as on the label of the bottle of wine below where one sees golden flowers drawn, of light and subtle way. Another example that I like is that of the bee of ree joined. Another modern idea identified on this site is this design: https://www.artpitchhub.example/design/52817304 https: //www.artpitchhub. example / design / 52817391 I would also need a round label to place on the lid of the pot with indications of signs (my address) as well as additional information about my product: - VALENTE Gaspard - Waldhofen, 14 - 6812 Brouvelle - 500 g - Spring harvest - Honey all flowers - Flora: rapeseed, fruit trees, clovers - Flavors: sweet honey with vegetal notes Remarks: this is my first artpitchhub project, if you are surprised by some points of the brief or it is missing important information do not hesitate to let me know! ************************************************** ******************************* ENGLISH ****************** ************** I need to beekeeper a new design Indeed, I work in a very natural environment, a high quality eco-system which is the south of Belgium (many different flowers in the fields, few pesticides, ...). I practice a natural beekeeping, in an artisanal way I produce a high quality honey (luxuous product) for wealthy people who are looking for good and healthy products. The following description: The Waldhofen Honey A slight variation could be useful for my production (alcohol from honey fermentation): The Waldhofen Meads Concerning the form, a modern design with golden patterns on a black background could be appropriate. An example is the honey of the wonders in attachment, we could see that honey in this case is a branded like a very luxuous product. I wish to go for these last colors with a more "rural touch" as attachment. We can see golden flowers in a light and elegant manner. Another interesting example is the honey bee in attachment. Some example found on this site: https://www.artpitchhub.example/design/52817304 https: //www.artpitchhub. example / design / 52817391 Valente Gaspard - Waldhofen, 14 - 6812 Brouvelle - 500 g - Spring Harvest - Honey all flowers - Flora: rapeseed, fruit, clovers - Flavors: sweet honey with vegetal notes

Target Market(s)

affluent clientele looking for natural products, good for health, ...

Industry/Entity Type

Agriculture

Font styles to use
Decorative
Script
Other font styles liked:
• à la libre appréciation du designer, tant que c'est moderne et élégant

Requirements
Must have
• All text must be in French / A main label and a round label on the lid of the jar. Gilding (preferably on a black background). An image accompanying the text. Gold on a black background
Nice to have
• Elegant and modern design Elegant and modern design
Should not have
• Do not load too much the main label, it must remain uncluttered

```html
<!DOCTYPE html>
<html lang="fr">
<head>
<meta charset="utf-8">
<title>Le miel du Waldhofen – étiquettes</title>
<link rel="stylesheet" href="https://fonts.googleapis.com/css2?family=EB+Garamond:wght@400;500&family=Roboto+Condensed:wght@400&display=swap">
<style>
  :root {
    --gold: #b59a5a;
    --gold-soft: rgba(181, 154, 90, 0.55);
    --black: #0b0b0b;
    --white: #ffffff;
    --paper: #ffffff;
    --caption: #111111;
  }
  * { margin: 0; padding: 0; box-sizing: border-box; }
  html, body { width: 1200px; height: 682px; overflow: hidden; background: var(--paper); }
  .board { position: relative; width: 1200px; height: 682px; font-family: "EB Garamond", Georgia, serif; }

  /* Lid labels */
  .lid-label { position: absolute; width: 300px; height: 560px; }
  .lid-label--spring { left: 54px; top: 48px; }
  .lid-label--summer { left: 832px; top: 48px; }
  .lid-tab {
    position: absolute; left: 122px; top: 292px; width: 66px; height: 212px;
    background: var(--black);
  }
  .lid-tab::before, .lid-tab::after {
    content: ""; position: absolute; top: 0; bottom: 0; width: 0;
    border-left: 1px dashed var(--gold);
  }
  .lid-tab::before { left: 8px; }
  .lid-tab::after { right: 8px; }
  .lid-disc { position: absolute; left: 0; top: 0; width: 300px; height: 300px; overflow: visible; }
  .lid-disc text { font-family: "EB Garamond", Georgia, serif; }
  .brand-small { fill: var(--gold); font-size: 15px; }
  .brand-large { fill: var(--gold); font-size: 30px; }
  .lid-tagline { fill: var(--white); font-size: 11px; letter-spacing: 1.1px; }
  .lid-info { fill: var(--white); font-size: 10.5px; font-weight: 500; }
  .lid-weight { fill: var(--white); font-size: 8.5px; }
  .lid-address { fill: var(--white); font-size: 11px; font-weight: 500; }

  /* Front label */
  .front-label { position: absolute; left: 423px; top: 180px; width: 334px; height: 230px; }
  .front-flora {
    position: absolute; left: 6px; top: 0; width: 322px; height: 92px; z-index: 0;
    background: radial-gradient(ellipse at 50% 100%, var(--gold-soft) 0%, rgba(181,154,90,0.25) 55%, rgba(181,154,90,0) 80%);
  }
  .front-body {
    position: absolute; left: 0; top: 92px; width: 334px; height: 138px; z-index: 1;
    background: var(--black); border-radius: 0 0 14px 14px;
    border-top: 9px solid var(--gold);
  }
  .front-brand {
    position: absolute; left: 0; top: 108px; width: 334px; z-index: 2;
    text-align: center; color: var(--gold); font-weight: 400; line-height: 1;
  }
  .front-brand__small { display: block; font-size: 16px; }
  .front-brand__large { display: block; font-size: 34px; margin-top: 2px; }
  .front-tagline {
    position: absolute; left: 0; top: 186px; width: 334px; z-index: 2; text-align: center;
    color: var(--gold); font-size: 12.5px; letter-spacing: 1.6px;
  }

  /* Captions */
  .caption {
    position: absolute; top: 588px; width: 300px; text-align: center;
    font-family: "Roboto Condensed", "Arial Narrow", sans-serif;
    font-size: 29px; color: var(--caption); letter-spacing: 0.3px;
  }
  .caption--spring { left: 48px; }
  .caption--summer { left: 822px; }
</style>
</head>
<body>
<main class="board">

  <section class="lid-label lid-label--spring" aria-label="Étiquette de couvercle – miel de printemps">
    <div class="lid-tab"></div>
    <svg class="lid-disc" viewBox="0 0 300 300">
      <defs><path id="arc-spring" d="M 32 150 A 118 118 0 0 0 268 150"/></defs>
      <circle cx="150" cy="150" r="142" fill="var(--gold)"/>
      <circle cx="150" cy="150" r="132" fill="var(--black)"/>
      <circle cx="150" cy="150" r="124" fill="none" stroke="var(--gold)" stroke-width="1" stroke-dasharray="5 4"/>
      <text class="brand-small" x="150" y="76" text-anchor="middle">Le miel du</text>
      <text class="brand-large" x="150" y="110" text-anchor="middle">Waldhofen</text>
      <text class="lid-tagline" x="150" y="162" text-anchor="middle">MIEL DOUX AUX NOTES VÉGÉTALES</text>
      <line x1="42" y1="170" x2="258" y2="170" stroke="var(--gold)" stroke-width="1.2"/>
      <text class="lid-info" x="150" y="187" text-anchor="middle">Récolte de printemps | Miel toutes fleurs</text>
      <text class="lid-info" x="150" y="201" text-anchor="middle">Flore : brassicacées, fruitiers, trèfle</text>
      <text class="lid-info" x="150" y="215" text-anchor="middle">Saveurs : miel doux aux</text>
      <text class="lid-info" x="150" y="229" text-anchor="middle">notes végétales</text>
      <text class="lid-weight" x="150" y="246" text-anchor="middle">- 500 g -</text>
      <text class="lid-address"><textPath href="#arc-spring" startOffset="50%" text-anchor="middle">VALENTE Gaspard / Waldhofen, 14 | 6812 Brouvelle</textPath></text>
    </svg>
  </section>

  <section class="front-label" aria-label="Étiquette principale">
    <div class="front-flora" role="img" aria-label="Motif floral doré de fleurs des champs et de rinceaux"></div>
    <div class="front-body"></div>
    <h1 class="front-brand"><span class="front-brand__small">Le miel du</span><span class="front-brand__large">Waldhofen</span></h1>
    <p class="front-tagline">MIEL DOUX AUX NOTES VÉGÉTALES</p>
  </section>

  <section class="lid-label lid-label--summer" aria-label="Étiquette de couvercle – miel d’été">
    <div class="lid-tab"></div>
    <svg class="lid-disc" viewBox="0 0 300 300">
      <defs><path id="arc-summer" d="M 32 150 A 118 118 0 0 0 268 150"/></defs>
      <circle cx="150" cy="150" r="142" fill="var(--gold)"/>
      <circle cx="150" cy="150" r="132" fill="var(--black)"/>
      <circle cx="150" cy="150" r="124" fill="none" stroke="var(--gold)" stroke-width="1" stroke-dasharray="5 4"/>
      <text class="brand-small" x="150" y="76" text-anchor="middle">Le miel du</text>
      <text class="brand-large" x="150" y="110" text-anchor="middle">Waldhofen</text>
      <text class="lid-tagline" x="150" y="162" text-anchor="middle">MIEL DOUX AUX NOTES VÉGÉTALES</text>
      <line x1="42" y1="170" x2="258" y2="170" stroke="var(--gold)" stroke-width="1.2"/>
      <text class="lid-info" x="150" y="187" text-anchor="middle">Récolte d’été | Miel toutes fleurs</text>
      <text class="lid-info" x="150" y="201" text-anchor="middle">Flore : ronces, trèfle, fruitiers, tilleul</text>
      <text class="lid-info" x="150" y="215" text-anchor="middle">Saveurs : miel doux aux</text>
      <text class="lid-info" x="150" y="229" text-anchor="middle">notes végétales</text>
      <text class="lid-weight" x="150" y="246" text-anchor="middle">- 500 g -</text>
      <text class="lid-address"><textPath href="#arc-summer" startOffset="50%" text-anchor="middle">VALENTE Gaspard / Waldhofen, 14 | 6812 Brouvelle</textPath></text>
    </svg>
  </section>

  <p class="caption caption--spring">SPRING HONEY</p>
  <p class="caption caption--summer">SUMMER HONEY</p>

</main>
</body>
</html>
```